Spa Business Card Design Project

Hello! We are a boutique spa for men and women that is rebranding. I would like a memorable new business card that showcases our beautiful new logo and our unique business. I would like it to be classic/timeless and eclectic/artistic at the  same time.
I am a fan of negative space as you can tell from the logo. I am also open to any creative ideas.
Multi sided design. Two sided design is acceptable as an option, too. "Flaps/folds/whatever the design term is" are optional- whether full vertical or horizontal, half flap, full flap etc
On either side next to the golden snail I would potentially like to see "slow down. Enjoy Life."  Possibly on one statment on top of each other, crowned with the snail. Or the statment following the snail on one line... I am open for a creative suprise, too.
The back I would like room for the standard Information
"3187 Birch Lane
Ashby, New York 12580
(518) 462 3058
info@thecorvale spa.com
The snail is to be done in gold ink.
Can I also Have an option for cards that are individualized for staff members, too?

Updates
Reason: I apologize for the deadline extension. My day was more involved than anticipated in other matters. Hope to have this closed by next Tuesday.
Thank you

Target Market(s)
Men and women with expendable income between the ages of 30-55
Industry/Entity Type
Boutique
Requirements
Must have
- only black and gold ink.

Nice to have
- One of a kind.
Showcase the snail :-)
make you smile :-)
Fun, but professional.
Should not have
- Lots of color.
Too feminine.
Too busy.

```html
<!DOCTYPE html>
<html lang="en">
<head>
<meta charset="utf-8">
<title>The Corvale Spa — Business Cards</title>
<link rel="stylesheet" href="https://fonts.googleapis.com/css2?family=Questrial&display=swap">
<style>
  :root {
    --ink: #1a1a1a;
    --gold: #d2ad69;
    --cream-light: #fbf8f0;
    --cream-deep: #efe3c8;
    --card-edge: #8c8c8c;
    --stage-center: #ffffff;
    --stage-edge: #f7f3e9;
  }
  * { box-sizing: border-box; margin: 0; padding: 0; }
  html, body { width: 1200px; height: 900px; overflow: hidden; }
  body {
    position: relative;
    background: radial-gradient(ellipse at 50% 50%, var(--stage-center) 55%, var(--stage-edge) 100%);
    font-family: "Questrial", "Helvetica Neue", Arial, sans-serif;
    color: var(--ink);
  }
  .card {
    position: absolute;
    width: 455px;
    height: 259px;
    background: #fff;
    border: 1px solid var(--card-edge);
    overflow: hidden;
  }
  .card-art { position: absolute; inset: 0; width: 100%; height: 100%; }

  /* front */
  .card--front { left: 373px; top: 124px; width: 454px; height: 260px; }
  .brand-name {
    position: absolute; left: 0; right: 0; top: 60px;
    text-align: center;
    font-size: 50px; font-weight: 400; line-height: 1.05; letter-spacing: 1px;
    color: var(--ink);
  }
  .tagline {
    position: absolute; left: 0; right: 0; top: 199px;
    text-align: center; font-size: 19px; color: var(--ink);
  }

  /* back */
  .card--back-general { left: 109px; top: 456px; }
  .card--back-staff { left: 634px; top: 456px; }
  .brand-mark {
    position: absolute; left: 40px; top: 70px; width: 130px;
    display: flex; flex-direction: column; align-items: center; gap: 6px;
  }
  .brand-mark__dot { width: 38px; height: 38px; border-radius: 50%; background: var(--gold); }
  .brand-mark__name { font-size: 12px; color: var(--ink); white-space: nowrap; }
  .motto {
    position: absolute; left: 40px; top: 156px; width: 130px;
    text-align: center; font-size: 16px; line-height: 22px;
  }
  .contact {
    position: absolute; left: 228px; top: 94px;
    font-size: 15.5px; line-height: 19px; list-style: none; white-space: nowrap;
  }
  .contact li.gap { margin-top: 6px; }
  .staff-name {
    position: absolute; left: 225px; top: 48px; font-size: 19px;
  }
  .card--back-staff .contact { left: 225px; top: 101px; }
</style>
</head>
<body>

<section class="card card--front" aria-label="Card front">
  <svg class="card-art" viewBox="0 0 454 260" preserveAspectRatio="none" aria-hidden="true">
    <defs>
      <radialGradient id="frontWash" cx="50%" cy="100%" r="80%">
        <stop offset="0" stop-color="var(--cream-light)"/>
        <stop offset="1" stop-color="var(--cream-deep)"/>
      </radialGradient>
    </defs>
    <path d="M0 110 C60 100 110 122 180 112 C250 102 320 120 380 110 C420 104 440 106 454 108 L454 260 L0 260 Z" fill="url(#frontWash)"/>
  </svg>
  <h1 class="brand-name">The Corvale<br>Spa</h1>
  <p class="tagline">a quiet day spa for Men &amp; Women</p>
</section>

<section class="card card--back-general" aria-label="Card back, general">
  <svg class="card-art" viewBox="0 0 455 259" preserveAspectRatio="none" aria-hidden="true">
    <defs>
      <linearGradient id="panelWashA" x1="0" y1="0" x2="1" y2="0">
        <stop offset="0" stop-color="var(--cream-light)"/>
        <stop offset="1" stop-color="var(--cream-deep)"/>
      </linearGradient>
    </defs>
    <path d="M183 0 C200 40 188 90 196 130 C204 175 196 220 205 259 L455 259 L455 0 Z" fill="url(#panelWashA)"/>
    <path d="M183 70 C196 110 196 160 186 205 C190 160 190 112 183 70 Z" fill="var(--gold)" stroke="var(--gold)" stroke-width="1.2"/>
  </svg>
  <div class="brand-mark"><span class="brand-mark__dot"></span><span class="brand-mark__name">The Corvale Spa</span></div>
  <p class="motto">Ease Up<br>Savor Life</p>
  <ul class="contact">
    <li>3187 Birch Lane</li>
    <li>Ashby, New York 12580</li>
    <li class="gap">518 · 462 · 3058</li>
    <li class="gap">info@thecorvalespa.com</li>
  </ul>
</section>

<section class="card card--back-staff" aria-label="Card back, staff">
  <svg class="card-art" viewBox="0 0 455 259" preserveAspectRatio="none" aria-hidden="true">
    <defs>
      <linearGradient id="panelWashB" x1="0" y1="0" x2="1" y2="0">
        <stop offset="0" stop-color="var(--cream-light)"/>
        <stop offset="1" stop-color="var(--cream-deep)"/>
      </linearGradient>
    </defs>
    <path d="M183 0 C200 40 188 90 196 130 C204 175 196 220 205 259 L455 259 L455 0 Z" fill="url(#panelWashB)"/>
    <path d="M183 70 C196 110 196 160 186 205 C190 160 190 112 183 70 Z" fill="var(--gold)" stroke="var(--gold)" stroke-width="1.2"/>
  </svg>
  <div class="brand-mark"><span class="brand-mark__dot"></span><span class="brand-mark__name">The Corvale Spa</span></div>
  <p class="motto">Ease Up<br>Savor Life</p>
  <p class="staff-name">Nora Ellison</p>
  <ul class="contact">
    <li>3187 Birch Lane</li>
    <li>Ashby, New York 12580</li>
    <li class="gap">518 · 462 · 3058</li>
    <li class="gap">info@thecorvalespa.com</li>
  </ul>
</section>

</body>
</html>
```